Email Signature

We would like to have an email Signature designed.
We have an idea, and a logo that we would like to be make more professional in design and look.

```html
<!DOCTYPE html>
<html lang="en">
<head>
<meta charset="utf-8">
<title>Email Signature – Tenmile Advisory</title>
<link href="https://fonts.googleapis.com/css2?family=Montserrat:wght@400;600;700&display=swap" rel="stylesheet">
<style>
  :root {
    --page: #ffffff;
    --card: #ffffff;
    --wave: #dcdcdd;
    --orange: #f05a28;
    --blue: #1a75c4;
    --ink: #3a3a3a;
  }
  * { margin: 0; padding: 0; box-sizing: border-box; }
  html, body {
    width: 1200px; height: 900px; overflow: hidden;
    background: var(--page);
    font-family: "Montserrat", sans-serif;
  }
  .canvas { position: relative; width: 1200px; height: 900px; }
  .signature {
    position: absolute; left: 85px; width: 1020px; height: 145px;
    background: var(--card);
    box-shadow: 0 2px 10px rgba(0,0,0,0.08);
    overflow: hidden;
  }
  .signature--first { top: 269px; }
  .signature--second { top: 477px; }
  .signature__decor {
    position: absolute; inset: 0;
    background: linear-gradient(100deg, rgba(220,220,221,0) 40%, var(--wave) 78%);
  }
  .contact { position: absolute; left: 28px; top: 36px; }
  .contact__name { color: var(--orange); font-weight: 600; font-size: 22px; line-height: 1.1; }
  .contact__role { color: var(--blue); font-weight: 600; font-size: 15px; margin-top: 2px; }
  .contact__phone { color: var(--ink); font-size: 18px; margin-top: 8px; }
  .contact__phone strong { font-weight: 700; }
  .brand {
    position: absolute; right: 66px; top: 52px;
    display: flex; flex-direction: column; align-items: flex-end;
  }
  .brand__row { display: flex; align-items: center; gap: 10px; }
  .brand__dot { width: 26px; height: 26px; border-radius: 50%; background: var(--orange); }
  .brand__name { color: var(--blue); font-weight: 700; font-size: 28px; letter-spacing: 0.5px; }
  .brand__web { color: var(--blue); font-weight: 700; font-size: 14px; margin-top: 18px; }
</style>
</head>
<body>
<main class="canvas">
  <section class="signature signature--first">
    <div class="signature__decor" role="img" aria-label="Decorative grey wave with orange and blue corner swoosh"></div>
    <div class="contact">
      <p class="contact__name">Kit Ramsden</p>
      <p class="contact__role">client relations</p>
      <p class="contact__phone">M: <strong>+61 400 555 182</strong></p>
    </div>
    <div class="brand">
      <div class="brand__row"><span class="brand__dot"></span><span class="brand__name">Tenmile Advisory</span></div>
      <span class="brand__web">www.tenmile.com.au</span>
    </div>
  </section>

  <section class="signature signature--second">
    <div class="signature__decor" role="img" aria-label="Decorative grey wave with long orange and blue corner swoosh"></div>
    <div class="contact">
      <p class="contact__name">Kit Ramsden</p>
      <p class="contact__role">client relations</p>
      <p class="contact__phone">M: <strong>+61 400 555 182</strong></p>
    </div>
    <div class="brand">
      <div class="brand__row"><span class="brand__dot"></span><span class="brand__name">Tenmile Advisory</span></div>
      <span class="brand__web">www.tenmile.com.au</span>
    </div>
  </section>
</main>
</body>
</html>
```